Global investment holding company - Business Card Design

Verin Crest is a recently incorporated investment holding company. Based in Singapore, it has operations in global emerging markets in the transport & logistics, energy and livestock industries.

Its tagline "Building Shared Futures" reflects the company's philosophy of helping countries progress through partnerships which generate employment and share benefits with its society.

We are looking for a business card that reflects our global presence - incorporating the logo design into the business card design. It must have a sophisticated, modern & corporate feel.

Target Market(s)

Investors and high level governmental officials

Industry/Entity Type

Investment

Requirements
Must have
• - Use of shades of blue in logo

-Profile picture

- Name: Dennis Oko
- Title: Chairman
- Email: dennis@verincrest-mail.com
- Mob: +65 9154 6021
- Tel: +65 6418 2095
- DID: + 65 6418 2096
- Address: 47 Harlow Road, #08-03, Singapore 058712

- website: www.verincrest-mail.com

```html
<!DOCTYPE html>
<html lang="en">
<head>
<meta charset="utf-8">
<title>Verin Crest – Business Card</title>
<link rel="stylesheet" href="https://fonts.googleapis.com/css2?family=Open+Sans:wght@400;600;700&display=swap">
<style>
  :root {
    --brand-blue: #1b4f93;
    --brand-blue-light: #5b8fcf;
    --ink-grey: #6f7275;
    --card-white: #ffffff;
    --page-bg: #e9eaec;
    --photo-tone-a: #c9b9a0;
    --photo-tone-b: #2c3442;
  }
  * { box-sizing: border-box; margin: 0; padding: 0; }
  html, body { width: 1200px; height: 880px; overflow: hidden; }
  body {
    background: var(--page-bg);
    font-family: "Open Sans", Arial, sans-serif;
    position: relative;
  }
  .card {
    position: absolute;
    left: 290px;
    width: 620px;
    height: 370px;
    background: var(--card-white);
    border-radius: 22px;
    border: 4px solid var(--brand-blue);
    overflow: hidden;
    box-shadow: 0 10px 28px rgba(0,0,0,0.18);
  }
  .card--back { top: 50px; }
  .card--front { top: 460px; }

  /* back side */
  .brand-lockup {
    position: absolute;
    left: 0; right: 0; top: 105px;
    display: flex; flex-direction: column; align-items: center;
  }
  .brand-row { display: flex; align-items: center; gap: 18px; }
  .brand-dot {
    flex: none;
    width: 78px; height: 78px; border-radius: 50%;
    background: var(--brand-blue);
  }
  .brand-name {
    font-weight: 700; color: var(--brand-blue);
    font-size: 44px; line-height: 1; text-transform: uppercase;
    white-space: nowrap;
  }
  .tagline {
    color: var(--ink-grey); font-size: 17px; letter-spacing: 2px;
    text-transform: uppercase; margin-top: 16px; white-space: nowrap;
  }
  .web-line {
    color: var(--ink-grey); font-size: 12px; letter-spacing: 4px; margin-top: 18px;
  }

  /* front side */
  .name-band {
    position: absolute; left: 0; right: 0; top: 138px; height: 46px;
    background: var(--brand-blue);
  }
  .person {
    position: absolute; left: 186px; top: 150px;
    color: var(--card-white); font-size: 20px; font-weight: 700; line-height: 24px;
    text-transform: uppercase; letter-spacing: 0.5px; white-space: nowrap;
  }
  .person .role {
    font-size: 12px; font-weight: 400; letter-spacing: 1px;
    border-left: 1px solid rgba(255,255,255,0.6);
    padding-left: 8px; margin-left: 8px;
  }
  .profile-photo {
    position: absolute; left: 40px; top: 28px; width: 128px; height: 136px;
    border: 5px solid var(--card-white);
    background: linear-gradient(180deg, var(--photo-tone-a) 0%, var(--photo-tone-a) 45%, var(--photo-tone-b) 100%);
    box-shadow: 0 3px 8px rgba(0,0,0,0.35);
  }
  .front-lockup {
    position: absolute; right: 40px; top: 34px;
    display: flex; flex-direction: column; align-items: flex-end;
  }
  .front-lockup .brand-dot { width: 50px; height: 50px; }
  .front-lockup .brand-name { font-size: 30px; }
  .front-lockup .tagline { font-size: 11px; letter-spacing: 1.5px; margin-top: 8px; }
  .contact-block {
    position: absolute; right: 40px; top: 202px;
    text-align: right; color: var(--brand-blue); font-size: 14px; line-height: 26px;
    white-space: nowrap;
  }
  .contact-block .label { color: var(--ink-grey); font-size: 12px; }
  .contact-block .sep { color: var(--brand-blue-light); margin: 0 6px; }
  .footer-band {
    position: absolute; left: 0; right: 0; top: 300px; height: 24px;
    background: var(--brand-blue);
  }
</style>
</head>
<body>
  <section class="card card--back" aria-label="Business card back">
    <div class="brand-lockup">
      <div class="brand-row">
        <span class="brand-dot"></span>
        <span class="brand-name">Verin Crest</span>
      </div>
      <p class="tagline">Building Shared Futures</p>
      <p class="web-line">www.verincrest-mail.com</p>
    </div>
  </section>

  <section class="card card--front" aria-label="Business card front">
    <div class="name-band"></div>
    <div class="profile-photo" role="img" aria-label="Profile photo of Dennis Oko"></div>
    <p class="person">Dennis Oko<span class="role">Chairman</span></p>
    <div class="front-lockup">
      <div class="brand-row">
        <span class="brand-dot"></span>
        <span class="brand-name">Verin Crest</span>
      </div>
      <p class="tagline">Building Shared Futures</p>
    </div>
    <div class="contact-block">
      <p>47 Harlow Road, #08-03, Singapore 058712</p>
      <p><span class="label">mobile:</span> +65 9154 6021<span class="sep">|</span><span class="label">tel:</span> +65 6418 2095<span class="sep">|</span><span class="label">did:</span> + 65 6418 2096</p>
      <p><span class="label">email:</span> dennis@verincrest-mail.com<span class="sep">|</span><span class="label">web:</span> www.verincrest-mail.com</p>
    </div>
    <div class="footer-band"></div>
  </section>
</body>
</html>
```